Modern logo for an International Trading & Consultating Company
KORVALEN INTERNATIONAL TRADING & CONSULTING
Modern logo for an International Trading & Consultating Company - Trade
Creative Brief
Simple
TAMIR BELQADI
BUSINESS DEVELOPER
Pelit Kavaklı İş Merkezi, Yeni Çınaraltı Cad. No: 14 34390 Beykoz İstanbul, Turkey
t.belqadi@korvalen-trading.example
Company's logo

```html
<!DOCTYPE html>
<html lang="en">
<head>
<meta charset="utf-8">
<title>Korvalen Business Cards</title>
<link href="https://fonts.googleapis.com/css2?family=Montserrat:wght@300;400;500;600&display=swap" rel="stylesheet">
<style>
  :root {
    --page: #ffffff;
    --card-light: #f4f4f3;
    --card-dark: #3a3330;
    --ink: #4a4a4a;
    --ink-soft: #777777;
    --gold: #b8975a;
    --logo-light: #5a5a5a;
    --logo-on-dark: #e6e1da;
  }
  * { margin: 0; padding: 0; box-sizing: border-box; }
  html, body {
    width: 1200px; height: 763px; overflow: hidden;
    background: var(--page);
    font-family: "Montserrat", sans-serif;
  }
  .canvas { position: relative; width: 1200px; height: 763px; }
  .card {
    position: absolute; left: 348px; width: 502px; height: 298px;
  }
  .card--front { top: 43px; background: var(--card-light); color: var(--ink); }
  .card--back { top: 421px; background: var(--card-dark); }

  .wordmark { position: absolute; left: 0; right: 0; text-align: center; font-weight: 300; }
  .wordmark__name { display: block; font-size: 42px; letter-spacing: 4px; line-height: 1; }
  .wordmark__tagline { display: block; font-size: 8.5px; letter-spacing: 2.6px; margin-top: 6px; }
  .card--front .wordmark { top: 78px; color: var(--logo-light); }
  .card--back .wordmark { top: 124px; color: var(--logo-on-dark); }

  .holder { position: absolute; left: 56px; top: 176px; }
  .holder__name { font-size: 10px; font-weight: 500; color: var(--gold); letter-spacing: 0.5px; }
  .holder__role { font-size: 6.5px; font-weight: 500; color: var(--ink); letter-spacing: 0.6px; margin-top: 4px; }
  .divider { position: absolute; left: 56px; right: 56px; top: 206px; height: 1px; background: var(--gold); }

  .address { position: absolute; left: 56px; top: 216px; font-size: 6.5px; line-height: 13px; color: var(--ink-soft); display: flex; gap: 14px; }
  .contact { position: absolute; left: 302px; top: 216px; font-size: 6.5px; line-height: 13px; color: var(--ink-soft); }
  .contact__row { display: flex; align-items: center; gap: 5px; }
  .contact__row svg { width: 7px; height: 7px; fill: var(--gold); }
</style>
</head>
<body>
<main class="canvas">
  <section class="card card--front" aria-label="Business card front">
    <div class="wordmark">
      <span class="wordmark__name">KORVALEN</span>
      <span class="wordmark__tagline">INTERNATIONAL TRADING &amp; CONSULTING</span>
    </div>
    <div class="holder">
      <p class="holder__name">TAMIR BELQADI</p>
      <p class="holder__role">BUSINESS DEVELOPER</p>
    </div>
    <div class="divider"></div>
    <div class="address">
      <p>Pelit Kavaklı<br>34390 Beykoz<br>İstanbul, Turkey</p>
      <p>İş Merkezi, Yeni Çınaraltı Cad. No: 14</p>
    </div>
    <div class="contact">
      <p class="contact__row">
        <svg viewBox="0 0 10 10" aria-hidden="true"><path d="M2 0.5 L3.8 2.8 L2.9 4 Q4 6 6 7.1 L7.2 6.2 L9.5 8 L8.3 9.5 Q3.5 9 0.5 1.7 Z"/></svg>
        +905550147280
      </p>
      <p class="contact__row">
        <svg viewBox="0 0 10 10" aria-hidden="true"><path d="M0.5 2 H9.5 V8 H0.5 Z M1 2.5 L5 5.5 L9 2.5" fill="none" stroke="#b8975a" stroke-width="1"/></svg>
        t.belqadi@korvalen-trading.example
      </p>
    </div>
  </section>

  <section class="card card--back" aria-label="Business card back">
    <div class="wordmark">
      <span class="wordmark__name">KORVALEN</span>
      <span class="wordmark__tagline">INTERNATIONAL TRADING &amp; CONSULTING</span>
    </div>
  </section>
</main>
</body>
</html>
```